5-star Hotel Web Design Project

I need a custom website design for a 5-star hotel. For full details please look at the attached ZIP archive.

The design should be in layers in Photoshop/Illustrator/InDesign format with all the icons/shapes/maps/graphic assets in vector format (svg, ai, eps) as much as possible.

I prefer white, simple but elegant websites. Please consider the performance/coding experience. We're not making something to show off our design skills on a design contest with fancy parallax effects and confusing animations. We're trying to create usable, functional and clean UI with good UX.

I would like to receive a few option for the color scheme to choose from.

The website will be custom coded, i.e. I'm not using WordPress.

NOTE: Don't bother to submit the generic WordPress style templates. We're looking for something custom made with attention to details. That's why the price is not guaranteed, but don't be mistaken, I'm a long time buyer here on SketchHive and all my projects are paid in full.

Low design quality

Europe

Hotel

5+ page

```html
<!DOCTYPE html>
<html lang="en">
<head>
<meta charset="utf-8">
<title>Coral Bay Resort</title>
<link rel="stylesheet" href="https://fonts.googleapis.com/css2?family=Roboto+Slab:wght@300;400;500;700&display=swap">
<style>
:root{
  --crimson:#a51c3f;
  --crimson-dark:#8e1634;
  --gold:#e0b55c;
  --ink:#222;
  --muted:#666;
  --line:#e3e3e3;
  --dark:#141414;
}
*{box-sizing:border-box;margin:0;padding:0}
html,body{width:1200px;height:2964px;overflow:hidden}
body{position:relative;font-family:"Roboto Slab",serif;color:var(--ink);background:#fff;font-size:13px}
.abs{position:absolute}
.header{top:0;left:0;width:1200px;height:75px;border-bottom:1px solid var(--line)}
.social-square{left:128px;top:23px;width:27px;height:27px;background:#cfa65a}
.brand{left:480px;top:16px;width:226px;text-align:center;color:var(--crimson);font-size:17px;line-height:1.2}
.brand .dot{display:inline-block;width:10px;height:10px;border-radius:50%;background:var(--gold);margin-right:6px;vertical-align:middle}
.lang{left:891px;top:23px;width:67px;height:29px;border:1px solid var(--crimson);color:var(--crimson);font-size:11px;display:flex;align-items:center;justify-content:center;gap:5px}
.book-top{left:965px;top:23px;width:107px;height:29px;background:var(--crimson);color:#fff;font-size:12px;display:flex;align-items:center;justify-content:center;gap:6px}
.nav{top:75px;left:0;width:1200px;height:38px;display:flex;justify-content:center;gap:37px;align-items:center;font-size:12px;color:#333}
.hero{top:113px;left:0;width:1200px;height:397px;background:linear-gradient(180deg,#9cc8ee 0%,#e8dcb0 28%,#d9c48c 45%,#4cb0d8 62%,#6aa84e 80%,#c85c6a 100%);border-bottom:8px solid var(--crimson)}
.booking{left:337px;top:481px;width:526px;height:60px;background:#fff;box-shadow:0 3px 12px rgba(0,0,0,.15);display:flex;align-items:center;padding:0 14px;gap:8px}
.field{width:192px;height:32px;border:1px solid var(--line);font-size:11px;color:#777;display:flex;align-items:center;padding-left:12px;gap:6px}
.btn-crimson{background:var(--crimson);color:#fff;font-size:11px;font-weight:500;display:flex;align-items:center;justify-content:center}
.intro-dots{left:420px;top:697px;width:185px;height:280px;background-image:radial-gradient(#d4d4d4 1.2px,transparent 1.4px);background-size:6px 6px}
.intro-photo{left:128px;top:612px;width:461px;height:348px;background:linear-gradient(160deg,#8cc6ef 0%,#3d8fb8 45%,#c8907c 70%,#e8e2dc 100%)}
.intro-text{left:670px;top:650px;width:402px}
.intro-text h2{color:var(--crimson);font-size:14px;font-weight:500;line-height:20px;text-transform:uppercase}
.intro-text .lead{color:var(--crimson);font-size:12.5px;line-height:20px;margin-top:13px}
.intro-text p{font-size:11px;line-height:18.5px;margin-top:15px;color:#333}
.btn-outline{display:inline-block;margin-top:22px;border:1px solid #999;font-size:10px;padding:8px 21px;color:#333}
.useful{top:1058px;left:0;width:1200px;height:363px;background:var(--crimson)}
.section-title{text-align:center;font-weight:500}
.stars{display:flex;justify-content:center;gap:4px;margin-top:6px}
.stars i{width:6px;height:6px;border-radius:50%;background:var(--gold);display:block}
.useful-title{left:128px;top:1102px;width:540px;color:var(--gold);font-size:19px}
.tile{width:117px;border:1px solid rgba(255,255,255,.22);color:#fff;font-size:11px;line-height:14px;text-align:center;display:flex;flex-direction:column;align-items:center;justify-content:flex-end;padding-bottom:10px;gap:8px}
.tile svg{width:26px;height:26px}
.tile.active{background:#d9ae66;color:var(--crimson);border-color:#d9ae66}
.slider{left:691px;top:1046px;width:381px;height:388px;background:#222;box-shadow:0 4px 14px rgba(0,0,0,.3)}
.slider-photo{left:0;top:0;width:381px;height:360px;background:radial-gradient(circle at 40% 40%,#f0c070 0%,#c87a34 50%,#8c4a1e 100%)}
.slider-caption{left:14px;top:253px;width:353px;height:102px;background:rgba(0,0,0,.88);padding:20px 0 0 21px;color:#fff}
.slider-caption h3{color:var(--gold);font-weight:400;font-size:24px}
.slider-caption p{font-size:12px;line-height:16px;margin-top:5px;width:200px}
.view-btn{left:250px;top:22px;width:82px;height:58px;border:1px solid var(--gold);color:var(--gold);font-size:14px;display:flex;align-items:center;justify-content:center}
.slider-dots{left:0;top:366px;width:381px;display:flex;justify-content:center;gap:8px}
.slider-dots i{width:9px;height:9px;border-radius:50%;border:1px solid #888;display:block}
.slider-dots i.on{border-color:var(--gold)}
.offer-title{left:0;top:1500px;width:1200px;color:var(--crimson);font-size:19px}
.offer-card{top:1563px;width:301px;height:197px}
.label{background:#fff;box-shadow:0 2px 8px rgba(0,0,0,.12);font-size:12.5px;display:flex;align-items:center;justify-content:center}
.label.on{background:var(--crimson);color:#fff}
.gallery{top:1856px;left:0;width:1200px;height:569px;background:linear-gradient(180deg,#eae4dc,#f2eee8 60%,#ebe5dd)}
.gallery-title{left:0;top:1921px;width:1200px;color:var(--crimson);font-size:19px}
.g-tile{width:218px;height:153px;border:2px solid #fff}
.partners-title{left:0;top:2490px;width:1200px;color:var(--crimson);font-size:19px}
.partner{top:2562px;width:174px;height:66px;background:#fff;box-shadow:0 2px 8px rgba(0,0,0,.08);display:flex;align-items:center;justify-content:center}
.partner span{display:block;width:84px;height:24px;background:#8a8a8a;border-radius:3px}
.newsletter{top:2761px;left:0;width:1200px;height:167px;background:linear-gradient(180deg,#1e1a1a,#0c0b0b 70%,#241812)}
.newsletter h3{position:absolute;top:50px;width:1200px;text-align:center;color:#fff;font-weight:400;font-size:20px}
.news-form{left:355px;top:83px;width:490px;height:40px;background:#fff;display:flex;align-items:center;padding:0 4px 0 14px;gap:8px;color:#aaa;font-size:11px}
.news-form .btn-crimson{margin-left:auto;width:117px;height:32px;font-size:12px;font-weight:400}
.footer{top:2928px;left:0;width:1200px;height:36px;background:var(--crimson);color:#fff;font-size:10.5px;display:flex;align-items:center;padding:0 130px}
.footer .sq{margin-left:auto;width:8px;height:10px;background:#fff}
</style>
</head>
<body>

<header class="abs header">
  <div class="abs social-square"></div>
  <div class="abs brand"><span class="dot"></span>Coral Bay Resort</div>
  <div class="abs lang">
    <svg width="10" height="10" viewBox="0 0 10 10"><circle cx="5" cy="5" r="4" fill="none" stroke="currentColor"/></svg>Eng ▾
  </div>
  <div class="abs book-top">
    <svg width="11" height="11" viewBox="0 0 11 11"><rect x="1" y="2" width="9" height="8" fill="none" stroke="#fff"/><line x1="1" y1="4.5" x2="10" y2="4.5" stroke="#fff"/></svg>Book Now
  </div>
</header>

<nav class="abs nav">
  <span>Coral Bay Resort</span><span>Accommodation</span><span>Restaurants &amp; Bars</span><span>Relax Center</span><span>Sport &amp; Entertainment</span><span>Events</span><span>Gallery</span><span>Contact Us</span>
</nav>

<div class="abs hero" role="img" aria-label="Aerial view of the resort buildings, pools and gardens beside the sea"></div>

<div class="abs booking">
  <div class="field">▦ Check-in date</div>
  <div class="field">▦ Check-out date</div>
  <div class="btn-crimson" style="width:100px;height:32px;margin-left:6px">BOOK NOW</div>
</div>

<div class="abs intro-dots"></div>
<div class="abs intro-photo" role="img" aria-label="Guest relaxing on a sailing boat with the sea and coastline behind"></div>
<div class="abs intro-text">
  <h2>New for summer 2021! The entrance to Coral Aquapark is included in the all inclusive package!</h2>
  <div class="lead">Feel and enjoy the emotional experience Coral Bay Resort &amp; Coral Aquapark!</div>
  <p>Coral Bay Resort is located right on a long, beautiful natural sandy beach in the quiet new quarter of Marenza. It is close to the main coastal motorway Saltport – Northhaven, which connects the hotel compound with the city of Saltport, the historic town of Old Castra, as well as with Golden Strand, the largest holiday destination on the Azure Coast.</p>
  <span class="btn-outline">READ MORE</span>
</div>

<section class="abs useful"></section>
<div class="abs section-title useful-title">USEFUL INFORMATION<div class="stars"><i></i><i></i><i></i><i></i><i></i></div></div>

<div class="abs tile" style="left:128px;top:1170px;height:86px"><svg viewBox="0 0 26 26"><rect x="6" y="8" width="14" height="12" rx="2" fill="none" stroke="var(--gold)" stroke-width="1.5" transform="rotate(-30 13 13)"/></svg>Prices for<br>Accommodation</div>
<div class="abs tile" style="left:260px;top:1170px;height:86px"><svg viewBox="0 0 26 26"><path d="M8 24V10M12 24V4M16 24V6M20 24V10" stroke="var(--gold)" stroke-width="1.5" fill="none"/></svg>All Inclusive<br>Program</div>
<div class="abs tile" style="left:392px;top:1170px;height:86px"><svg viewBox="0 0 26 26"><rect x="6" y="4" width="14" height="18" fill="none" stroke="var(--gold)" stroke-width="1.5"/><path d="M9 9h8M9 13h8M9 17h8" stroke="var(--gold)"/></svg>Brochure</div>
<div class="abs tile" style="left:523px;top:1170px;height:86px"><svg viewBox="0 0 26 26"><path d="M3 20h20M4 20v-8h18v8M6 12V8h14v4" fill="none" stroke="var(--gold)" stroke-width="1.5"/></svg>Hotel fact<br>Sheet</div>
<div class="abs tile" style="left:128px;top:1271px;height:95px"><svg viewBox="0 0 26 26"><path d="M2 13l6-5 5 4 5-4 6 5-6 5-5-4-5 4z" fill="none" stroke="var(--gold)" stroke-width="1.5"/></svg>Company Details</div>
<div class="abs tile" style="left:260px;top:1271px;height:95px"><svg viewBox="0 0 26 26"><path d="M13 20s-6-6-6-10a6 6 0 0112 0c0 4-6 10-6 10z" fill="none" stroke="var(--gold)" stroke-width="1.5"/><circle cx="13" cy="10" r="2" fill="var(--gold)"/></svg>Map</div>
<div class="abs tile active" style="left:392px;top:1271px;height:95px"><svg viewBox="0 0 26 26"><path d="M4 20h18M6 20c0-5 3-8 7-8s7 3 7 8" fill="none" stroke="var(--crimson)" stroke-width="1.5"/></svg>Relax Center</div>
<div class="abs tile" style="left:523px;top:1271px;height:95px"><svg viewBox="0 0 26 26"><circle cx="13" cy="11" r="6" fill="none" stroke="var(--gold)" stroke-width="1.5"/><path d="M5 22h16" stroke="var(--gold)" stroke-width="1.5"/></svg>Prices for<br>extra services</div>

<div class="abs slider">
  <div class="abs slider-photo" role="img" aria-label="Two children lying among daisies, seen from above"></div>
  <div class="abs slider-caption">
    <h3>EASTER OFFER</h3>
    <p>The best holidays are those spent in our resort</p>
    <div class="abs view-btn">View</div>
  </div>
  <div class="abs slider-dots"><i></i><i class="on"></i><i></i><i></i><i></i></div>
</div>

<div class="abs section-title offer-title">SPECIAL OFFER<div class="stars"><i></i><i></i><i></i><i></i><i></i></div></div>
<div class="abs offer-card" style="left:128px;background:linear-gradient(180deg,#7a5a2e,#3c3a22)" role="img" aria-label="Conference hall with rows of chairs"></div>
<div class="abs offer-card" style="left:450px;background:linear-gradient(180deg,#d8c48a,#efe6c8)" role="img" aria-label="Banquet tables set for a wedding"></div>
<div class="abs offer-card" style="left:771px;background:linear-gradient(180deg,#b8281c,#6a1a14)" role="img" aria-label="Stage with a podium and trophy for an event"></div>
<div class="abs label" style="left:169px;top:1741px;width:219px;height:45px">Business Offer</div>
<div class="abs label on" style="left:491px;top:1727px;width:219px;height:45px">For your wedding</div>
<div class="abs label" style="left:812px;top:1741px;width:219px;height:45px">Events</div>

<section class="abs gallery"></section>
<div class="abs section-title gallery-title">Gallery<div class="stars"><i></i><i></i><i></i></div></div>

<div class="abs g-tile" style="left:128px;top:1994px;background:linear-gradient(180deg,#c8ccd0,#5aa8c8)" role="img" aria-label="Aerial view of resort pools"></div>
<div class="abs g-tile" style="left:369px;top:1994px;background:linear-gradient(180deg,#d8d0b0,#6aa048)" role="img" aria-label="Aparthotel arches and palm trees"></div>
<div class="abs g-tile" style="left:611px;top:1994px;background:linear-gradient(180deg,#d0c8bc,#7a3a2a)" role="img" aria-label="Hotel room with a double bed"></div>
<div class="abs g-tile" style="left:853px;top:1994px;background:linear-gradient(180deg,#3a2418,#d8c8b0)" role="img" aria-label="Diners at a set restaurant table"></div>
<div class="abs g-tile" style="left:128px;top:2186px;background:linear-gradient(180deg,#e0902a,#b85a14)" role="img" aria-label="Spa relaxation loungers"></div>
<div class="abs g-tile" style="left:369px;top:2186px;background:linear-gradient(180deg,#1a1a2a,#2a4a7a)" role="img" aria-label="Billiards room"></div>
<div class="abs g-tile" style="left:611px;top:2186px;background:linear-gradient(180deg,#2a2a2a,#7a7a7a)" role="img" aria-label="Conference hall with seats"></div>
<div class="abs g-tile" style="left:853px;top:2186px;background:linear-gradient(180deg,#7a1a1a,#3a2a2a)" role="img" aria-label="Group at an event with a trophy"></div>

<div class="abs label" style="left:146px;top:2126px;width:184px;height:37px">Coral Bay Resort</div>
<div class="abs label" style="left:388px;top:2126px;width:184px;height:37px">Aparthotels</div>
<div class="abs label" style="left:629px;top:2126px;width:184px;height:37px">Accommodation</div>
<div class="abs label" style="left:870px;top:2126px;width:184px;height:37px">Food &amp; Beverage</div>
<div class="abs label" style="left:146px;top:2318px;width:184px;height:37px">Relax &amp; Wellness</div>
<div class="abs label" style="left:388px;top:2318px;width:184px;height:37px">Sport &amp; Entertainment</div>
<div class="abs label on" style="left:629px;top:2311px;width:184px;height:37px">Conference halls</div>
<div class="abs label" style="left:870px;top:2318px;width:184px;height:37px">Events</div>

<div class="abs section-title partners-title">Become a partner<div class="stars"><i></i><i></i><i></i><i></i><i></i></div></div>
<div class="abs partner" style="left:130px"><span></span></div>
<div class="abs partner" style="left:322px"><span></span></div>
<div class="abs partner" style="left:513px"><span></span></div>
<div class="abs partner" style="left:704px"><span></span></div>
<div class="abs partner" style="left:896px"><span></span></div>

<svg class="abs" style="left:566px;top:2671px" width="100" height="22" viewBox="0 0 100 22">
  <path d="M22 11H4M4 11l5-4M4 11l5 4" stroke="#444" stroke-width="1.3" fill="none"/>
  <rect x="37" y="0" width="38" height="22" fill="var(--crimson)"/>
  <path d="M47 11h18M65 11l-5-4M65 11l-5 4" stroke="#fff" stroke-width="1.3" fill="none"/>
</svg>

<section class="abs newsletter">
  <h3>Subscribe to our Newsletter.</h3>
  <div class="abs news-form">
    <svg width="18" height="14" viewBox="0 0 18 14"><rect x="1" y="1" width="16" height="12" fill="none" stroke="#bbb"/><path d="M1 1l8 6 8-6" fill="none" stroke="#bbb"/></svg>
    enter your email address here...
    <div class="btn-crimson">Subscribe Now</div>
  </div>
</section>

<footer class="abs footer">
  Copyright © 2021 Coral Bay Resort. All Rights Reserved
  <span class="sq"></span>
</footer>

</body>
</html>
```